National Training and assessment company needs a website

Create a 4 page website, simple but professional, the company provides training services to industry, resumes'/ CVs, personnel skill assessment, workplace skills profiling and develops manufactures and supplies training equipment for electrical/engineering training, Company title is Corvan T Pty Ltd and also trades under RSK & Associates. letterheads etc all are done using dark green
Updates
Project Deadline Extended
Reason: Due to work commitments will be interstate from the 26/02 til 05/03/14
Target Market(s)
The market is broad covering the general public, secondary colleges and corporate sector
Industry/Entity Type
Training
Look and feel
Each slider illustrates characteristics of the customer's brand and the style your logo design should communicate.

```html
<!DOCTYPE html>
<html lang="en">
<head>
<meta charset="utf-8">
<title>RSK &amp; Associates — Training and Assessment</title>
<link rel="stylesheet" href="https://fonts.googleapis.com/css2?family=Tinos:wght@400;700&display=swap">
<style>
  :root {
    --page-bg: #f4f4f4;
    --column-bg: #ffffff;
    --brand-green: #3cb44b;
    --brand-blue: #0a80c8;
    --hero-band: #e6e6e6;
    --hero-light: #f3f5f6;
    --hero-mid: #e7ebed;
    --nav-band: #dde3ea;
    --card-bg: #ebebeb;
    --text-dark: #333333;
    --text-body: #4a4a4a;
  }
  * { box-sizing: border-box; margin: 0; padding: 0; }
  html, body {
    width: 1200px;
    height: 854px;
    overflow: hidden;
  }
  body {
    position: relative;
    background: var(--page-bg);
    font-family: "Tinos", "Times New Roman", serif;
    color: var(--text-dark);
  }
  .column {
    position: absolute;
    left: 163px;
    top: 0;
    width: 975px;
    height: 854px;
    background: var(--column-bg);
  }
  .brand {
    position: absolute;
    left: 193px;
    top: 10px;
    color: var(--brand-green);
    font-size: 31px;
    font-weight: 400;
    line-height: 36px;
  }
  .brand .brand-line2 { display: block; padding-left: 16px; }

  .hero-band {
    position: absolute;
    left: 0;
    top: 85px;
    width: 1200px;
    height: 319px;
    background: var(--hero-band);
  }
  .hero-visual {
    position: absolute;
    left: 163px;
    top: 85px;
    width: 975px;
    height: 319px;
    background: linear-gradient(90deg, var(--hero-mid) 0%, var(--hero-light) 35%, var(--hero-light) 65%, var(--hero-mid) 100%);
  }
  .hero-copy {
    position: absolute;
    left: 193px;
    top: 132px;
    color: var(--brand-blue);
  }
  .hero-lead { font-size: 35px; line-height: 42px; font-weight: 400; }
  .hero-title { font-size: 45px; line-height: 52px; font-weight: 400; }
  .services {
    list-style: none;
    margin-top: 10px;
    color: var(--text-dark);
    font-size: 19.5px;
    line-height: 30px;
  }
  .services li { position: relative; padding-left: 26px; }
  .services li::before {
    content: "";
    position: absolute;
    left: 2px;
    top: 13px;
    width: 6px;
    height: 6px;
    border-radius: 50%;
    background: var(--text-dark);
  }

  .main-nav {
    position: absolute;
    left: 0;
    top: 404px;
    width: 1200px;
    height: 39px;
    background: var(--nav-band);
  }
  .main-nav ul {
    list-style: none;
    display: flex;
    position: absolute;
    left: 190px;
    top: 12px;
    font-size: 14.5px;
    color: var(--brand-blue);
    letter-spacing: 0.3px;
  }
  .main-nav li + li::before {
    content: "|";
    margin: 0 12px;
  }

  .card {
    position: absolute;
    top: 472px;
    width: 457px;
    height: 283px;
    background: var(--card-bg);
    padding: 16px 15px 0 15px;
  }
  .card-left { left: 178px; }
  .card-right { left: 663px; }
  .card-head { display: flex; align-items: center; height: 37px; }
  .card-icon { width: 37px; height: 37px; flex: none; }
  .card-title {
    margin-left: 15px;
    color: var(--brand-blue);
    font-size: 19px;
    font-weight: 400;
    letter-spacing: 0.2px;
  }
  .card-text {
    margin-top: 17px;
    color: var(--text-body);
    font-size: 13.3px;
    line-height: 16.9px;
  }
  .card-text + .card-text { margin-top: 17px; }

  .social {
    position: absolute;
    left: 573px;
    top: 790px;
    display: flex;
    gap: 14px;
  }
  .social a { display: block; width: 42px; height: 42px; }
</style>
</head>
<body>
  <div class="column"></div>

  <header>
    <div class="brand">RSK<span class="brand-line2">&amp; Associates</span></div>
  </header>

  <div class="hero-band"></div>
  <div class="hero-visual" role="img" aria-label="Photo: a hand drawing a cloud with the word goal on a whiteboard"></div>
  <section class="hero-copy">
    <h1>
      <span class="hero-lead" style="display:block">Attend our trainings and</span>
      <span class="hero-title" style="display:block">Achieve your goals!</span>
    </h1>
    <ul class="services">
      <li>Employer Workplace skills profiling</li>
      <li>Employee skills profiling (Competency Profiling)</li>
      <li>Workplace training and Assessment</li>
      <li>Resume and Curricula Vita compilation</li>
    </ul>
  </section>

  <nav class="main-nav">
    <ul>
      <li>HOME</li>
      <li>PROGRAMS</li>
      <li>TRAININGS</li>
      <li>CONTACTS</li>
    </ul>
  </nav>

  <article class="card card-left">
    <div class="card-head">
      <svg class="card-icon" viewBox="0 0 37 37" aria-hidden="true"><circle cx="18.5" cy="18.5" r="18.5" fill="#0a80c8"/></svg>
      <h2 class="card-title">TITLE WITH ICON</h2>
    </div>
    <p class="card-text">Maecenas adipiscing augue magna, eget adipiscing leo bibendum et. Donec fringilla rhoncus feugiat. Integer posuere feugiat viverra. Morbi at nisi non nisl suscipit rutrum. Praesent iaculis metus arcu, non molestie lectus congue vel. Sed congue, neque tempor aliquam dictum, est est feugiat felis, ac cursus urna diam nec neque. Class aptent taciti sociosqu ad litora torquent per conubia nostra, per inceptos himenaeos.</p>
    <p class="card-text">Quisque facilisis rhoncus suscipit. Praesent velit nulla, aliquam dictum rhoncus sit amet, venenatis et lacus. Donec laoreet urna non interdum faucibus.</p>
  </article>

  <article class="card card-right">
    <div class="card-head">
      <svg class="card-icon" viewBox="0 0 37 37" aria-hidden="true"><circle cx="18.5" cy="18.5" r="18.5" fill="#0a80c8"/></svg>
      <h2 class="card-title">TITLE WITH ICON</h2>
    </div>
    <p class="card-text">Maecenas adipiscing augue magna, eget adipiscing leo bibendum et. Donec fringilla rhoncus feugiat. Integer posuere feugiat viverra. Morbi at nisi non nisl suscipit rutrum. Praesent iaculis metus arcu, non molestie lectus congue vel. Sed congue, neque tempor aliquam dictum, est est feugiat felis, ac cursus urna diam nec neque. Class aptent taciti sociosqu ad litora torquent per conubia nostra, per inceptos himenaeos.</p>
    <p class="card-text">Quisque facilisis rhoncus suscipit. Praesent velit nulla, aliquam dictum rhoncus sit amet, venenatis et lacus. Donec laoreet urna non interdum faucibus.</p>
  </article>

  <footer class="social">
    <a aria-label="Social link one"><svg viewBox="0 0 42 42" width="42" height="42"><circle cx="21" cy="21" r="21" fill="#0a80c8"/></svg></a>
    <a aria-label="Social link two"><svg viewBox="0 0 42 42" width="42" height="42"><circle cx="21" cy="21" r="21" fill="#0a80c8"/></svg></a>
    <a aria-label="Social link three"><svg viewBox="0 0 42 42" width="42" height="42"><circle cx="21" cy="21" r="21" fill="#0a80c8"/></svg></a>
  </footer>
</body>
</html>
```